Company service wheel graphic

A graphic demonstrating all the services the company offers.
I have hand drawn and written up on the attached the content that is required. Also attached is our company logo so you have a sense of the colour scheme of the logo.
This will eventually go into a company brochure, be used on our website etc.

Target Market(s)

Local GOvernment and other professionals who work in the sport, recreation and leisure industries

Industry/Entity Type

Sports, recreation, leisure, aquatics

Font styles to use
Other font styles liked:
• Calibri

Colors
0054AA
0677BA
7BADD7
CADEEF
E8F1F8

Requirements
Must have
• An eye catching graphic that captures all the information in the hand drawn atachement.
Nice to have
• Each quadrant in the circle to have its own colour, that links to the company logo

```html
<!DOCTYPE html>
<html lang="en">
<head>
<meta charset="utf-8">
<title>Service Wheel</title>
<link href="https://fonts.googleapis.com/css2?family=Rubik:wght@400;500;700&display=swap" rel="stylesheet">
<style>
  :root {
    --navy: #1d1a5b;
    --blue: #0b5b8f;
    --ring: #1f3f63;
    --white: #ffffff;
    --ink: #111111;
  }
  html, body {
    margin: 0;
    padding: 0;
    width: 1200px;
    height: 1006px;
    overflow: hidden;
    background: var(--white);
  }
  .service-wheel {
    display: block;
    width: 1200px;
    height: 1006px;
    font-family: "Rubik", sans-serif;
  }
  .audience-text {
    font-size: 21px;
    font-weight: 500;
    letter-spacing: 5.2px;
    fill: var(--navy);
  }
  .item { font-size: 13.5px; font-weight: 400; }
  .item--light { fill: var(--white); }
  .item--blue { fill: var(--blue); }
  .item--small { font-size: 11.5px; }
  .bullet--light { color: var(--white); }
  .bullet--blue { color: var(--blue); }
  .hub-title {
    font-size: 22.5px;
    font-weight: 700;
    text-anchor: middle;
  }
  .hub-title--navy { fill: var(--navy); }
  .hub-title--blue { fill: var(--blue); }
  .stage-label {
    font-size: 12.5px;
    font-weight: 700;
    fill: var(--white);
    letter-spacing: 0.4px;
  }
  .stage-label--small { font-size: 11px; }
  .engagement-label {
    font-size: 13px;
    font-weight: 700;
    fill: var(--ink);
  }
  .brand-name {
    font-size: 19px;
    font-weight: 500;
    fill: var(--blue);
    text-anchor: middle;
  }
</style>
</head>
<body>
<svg class="service-wheel" viewBox="0 0 1200 1006" xmlns="http://www.w3.org/2000/svg">
  <defs>
    <symbol id="bullet-arrow" viewBox="-9 -9 18 18">
      <path d="M-2.5 -6.5 A7 7 0 1 1 -2.5 6.5" fill="none" stroke="currentColor" stroke-width="1.8"/>
      <path d="M-7 -3.2 H0 L-2 -6 L5 0 L-2 6 L0 3.2 H-7 Z" fill="currentColor"/>
    </symbol>
    <path id="audience-top" d="M209 645 A416 416 0 1 1 991 645"/>
    <path id="audience-bottom" d="M193 355 A433 433 0 1 0 1007 355"/>
    <path id="arc-planning" d="M492 503 A108 108 0 0 1 600 395"/>
    <path id="arc-management" d="M600 395 A108 108 0 0 1 708 503"/>
    <path id="arc-growing" d="M478 503 A122 122 0 0 0 600 625"/>
    <path id="arc-impact-1" d="M600 622 A119 119 0 0 0 719 503"/>
    <path id="arc-impact-2" d="M600 635 A132 132 0 0 0 732 503"/>
    <path id="arc-engagement" d="M530 530 A74 74 0 1 1 670 530"/>
  </defs>

  <!-- outer audience ring -->
  <circle class="outer-ring" cx="600" cy="503" r="462" fill="none" stroke="var(--ring)" stroke-width="1.5"/>
  <text class="audience-text"><textPath href="#audience-top" startOffset="50%" text-anchor="middle">LOCAL + STATE GOVERNMENT. SPORT + LEISURE FACILITY MANAGERS</textPath></text>
  <text class="audience-text"><textPath href="#audience-bottom" startOffset="50%" text-anchor="middle">INVESTORS + DEVELOPERS, ARCHITECTS + DESIGNERS SPORT + RECREATION + COMMUNITY PROVIDERS</textPath></text>

  <!-- quadrants -->
  <path class="quadrant quadrant--planning" d="M587 490 V123 A367 367 0 0 0 220 490 Z" fill="var(--navy)" stroke="var(--navy)" stroke-width="20" stroke-linejoin="round"/>
  <path class="quadrant quadrant--management" d="M613 490 V123 A367 367 0 0 1 980 490 Z" fill="var(--navy)" stroke="var(--navy)" stroke-width="20" stroke-linejoin="round"/>
  <path class="quadrant quadrant--growing" d="M598 880 V520 Q598 506 584 506 H226 Q212 506 212 522 A386.5 386.5 0 0 0 582 892 Q598 892 598 880 Z" fill="var(--white)" stroke="var(--blue)" stroke-width="2.5"/>
  <path class="quadrant quadrant--impact" d="M602 880 V520 Q602 506 616 506 H974 Q988 506 988 522 A386.5 386.5 0 0 1 618 892 Q602 892 602 880 Z" fill="var(--white)" stroke="var(--blue)" stroke-width="2.5"/>

  <!-- hub: top stem -->
  <line x1="465" y1="430" x2="465" y2="502" stroke="var(--white)" stroke-width="2.5"/>
  <line x1="735" y1="430" x2="735" y2="502" stroke="var(--white)" stroke-width="2.5"/>
  <polygon class="hub-box hub-box--facilities" points="435,303 765,303 765,333 738,362 462,362 435,333" fill="var(--white)"/>
  <line x1="600" y1="362" x2="600" y2="420" stroke="var(--white)" stroke-width="3"/>
  <text class="hub-title hub-title--navy" x="600" y="326">Community, Aquatic +</text>
  <text class="hub-title hub-title--navy" x="600" y="355">Recreation facilities</text>

  <!-- hub: bottom stem -->
  <rect class="hub-stem" x="465" y="506" width="270" height="130" fill="var(--blue)"/>
  <line x1="600" y1="506" x2="600" y2="640" stroke="var(--white)" stroke-width="3"/>
  <circle cx="477" cy="615" r="39" fill="var(--blue)"/>
  <circle cx="723" cy="615" r="39" fill="var(--blue)"/>
  <polygon class="hub-box hub-box--activation" points="456,645 744,645 768,668 768,708 432,708 432,668" fill="var(--white)" stroke="var(--blue)" stroke-width="2.5"/>
  <text class="hub-title hub-title--blue" x="600" y="682">Community Activation</text>

  <!-- stage icon circles -->
  <circle cx="481" cy="393" r="40" fill="var(--navy)"/>
  <g class="icon icon--checklist" fill="none" stroke="var(--white)" stroke-width="1.8">
    <path d="M458 370 H484 L492 378 V418 H458 Z"/>
    <rect x="463" y="381" width="5" height="5"/>
    <rect x="463" y="392" width="5" height="5"/>
    <rect x="463" y="403" width="5" height="5"/>
    <path d="M472 383 H486 M472 394 H486 M472 405 H484"/>
    <path d="M500 380 L490 412 L492 416 L495 413 L505 382 Z"/>
  </g>
  <circle cx="722" cy="393" r="40" fill="var(--navy)"/>
  <g class="icon icon--gear" fill="none" stroke="var(--white)">
    <circle cx="722" cy="393" r="9" stroke-width="2"/>
    <circle cx="722" cy="393" r="14" stroke-width="5" stroke-dasharray="4 3.3"/>
    <circle cx="722" cy="393" r="13" stroke-width="1.6"/>
    <path d="M697 400 A26 26 0 0 1 738 372" stroke-width="2"/>
    <path d="M747 386 A26 26 0 0 1 706 414" stroke-width="2"/>
  </g>
  <g class="icon icon--hands" fill="none" stroke="var(--white)" stroke-width="1.8" stroke-linejoin="round">
    <path d="M469 630 V606 M474 604 V600 M478 600 V598 M482 600 V604 M486 604 V616 L492 610"/>
    <path d="M469 606 Q468 600 474 600 Q474 594 478 596 Q482 592 482 600 Q486 598 486 604"/>
    <rect x="467" y="630" width="22" height="8"/>
    <path d="M452 602 L464 614 M502 602 L490 614 M455 596 L449 602 M499 596 L505 602"/>
  </g>
  <g class="icon icon--people" fill="none" stroke="var(--white)" stroke-width="2">
    <circle cx="711" cy="608" r="5"/>
    <circle cx="725" cy="606" r="5.5"/>
    <circle cx="739" cy="608" r="5"/>
    <path d="M702 628 Q702 616 711 616 Q716 616 718 620"/>
    <path d="M714 630 Q714 615 725 615 Q736 615 736 630"/>
    <path d="M748 628 Q748 616 739 616 Q734 616 732 620"/>
  </g>

  <!-- centre -->
  <circle class="hub-core" cx="600" cy="503" r="95" fill="var(--white)"/>
  <text class="engagement-label"><textPath href="#arc-engagement" startOffset="50%" text-anchor="middle">Community + Stakeholder Engagement</textPath></text>
  <circle cx="600" cy="510" r="43" fill="none" stroke="var(--blue)" stroke-width="1"/>
  <text class="brand-name" x="600" y="517">VELQUORA</text>

  <!-- stage labels -->
  <text class="stage-label"><textPath href="#arc-planning" startOffset="55%" text-anchor="middle">PLANNING</textPath></text>
  <text class="stage-label"><textPath href="#arc-management" startOffset="48%" text-anchor="middle">MANAGEMENT</textPath></text>
  <text class="stage-label"><textPath href="#arc-growing" startOffset="50%" text-anchor="middle">GROWING PARTICIPATION</textPath></text>
  <text class="stage-label stage-label--small"><textPath href="#arc-impact-1" startOffset="50%" text-anchor="middle">COMMUNITY IMPACT</textPath></text>
  <text class="stage-label stage-label--small"><textPath href="#arc-impact-2" startOffset="50%" text-anchor="middle">+PARTICIPATIONS</textPath></text>

  <!-- planning services -->
  <g class="service-list service-list--planning">
    <use href="#bullet-arrow" class="bullet--light" x="370" y="217" width="16" height="16"/>
    <text class="item item--light" x="395" y="229">Feasibility Studies</text>
    <use href="#bullet-arrow" class="bullet--light" x="320" y="261" width="16" height="16"/>
    <text class="item item--light" x="347" y="274">Community + Stakeholder</text>
    <text class="item item--light" x="347" y="292">research</text>
    <use href="#bullet-arrow" class="bullet--light" x="275" y="331" width="16" height="16"/>
    <text class="item item--light" x="301" y="339">Sport + Recreation</text>
    <text class="item item--light" x="301" y="357">strategies</text>
    <use href="#bullet-arrow" class="bullet--light" x="254" y="388" width="16" height="16"/>
    <text class="item item--light" x="281" y="402">Design strategies</text>
    <use href="#bullet-arrow" class="bullet--light" x="243" y="432" width="16" height="16"/>
    <text class="item item--light" x="271" y="443">Indoor + Outdoor</text>
    <text class="item item--light" x="271" y="461">spaces</text>
  </g>

  <!-- management services -->
  <g class="service-list service-list--management">
    <use href="#bullet-arrow" class="bullet--light" x="643" y="195" width="16" height="16"/>
    <text class="item item--light" x="672" y="205">Activating</text>
    <text class="item item--light" x="672" y="223">underutilised assets</text>
    <use href="#bullet-arrow" class="bullet--light" x="643" y="243" width="16" height="16"/>
    <text class="item item--light" x="672" y="250">Income + revenue</text>
    <text class="item item--light" x="672" y="268">generation strategies</text>
    <use href="#bullet-arrow" class="bullet--light" x="783" y="310" width="16" height="16"/>
    <text class="item item--light" x="806" y="320">Mystery Shopper +</text>
    <text class="item item--light" x="806" y="338">business health</text>
    <text class="item item--light" x="806" y="356">checks</text>
    <use href="#bullet-arrow" class="bullet--light" x="783" y="382" width="16" height="16"/>
    <text class="item item--light" x="810" y="390">Financial +</text>
    <text class="item item--light" x="810" y="408">funding strategies</text>
    <use href="#bullet-arrow" class="bullet--light" x="783" y="427" width="16" height="16"/>
    <text class="item item--light" x="810" y="441">Management Support</text>
    <use href="#bullet-arrow" class="bullet--light" x="783" y="463" width="16" height="16"/>
    <text class="item item--light" x="810" y="477">Business Planning</text>
  </g>

  <!-- growing participation services -->
  <g class="service-list service-list--growing">
    <use href="#bullet-arrow" class="bullet--blue" x="237" y="526" width="16" height="16"/>
    <text class="item item--blue" x="265" y="540">Trends + Insights</text>
    <use href="#bullet-arrow" class="bullet--blue" x="241" y="565" width="16" height="16"/>
    <text class="item item--blue" x="268" y="578">Health profiling</text>
    <use href="#bullet-arrow" class="bullet--blue" x="252" y="604" width="16" height="16"/>
    <text class="item item--blue" x="283" y="614">Active recreation</text>
    <text class="item item--blue" x="283" y="632">strategies</text>
    <use href="#bullet-arrow" class="bullet--blue" x="283" y="657" width="16" height="16"/>
    <text class="item item--blue" x="316" y="667">Community</text>
    <text class="item item--blue" x="316" y="685">program</text>
    <text class="item item--blue" x="316" y="703">development</text>
    <use href="#bullet-arrow" class="bullet--blue" x="334" y="730" width="16" height="16"/>
    <text class="item item--blue" x="368" y="739">Physical activity</text>
    <text class="item item--blue" x="368" y="757">strategies</text>
    <use href="#bullet-arrow" class="bullet--blue" x="386" y="781" width="16" height="16"/>
    <text class="item item--blue" x="413" y="788">Specific cohort</text>
    <text class="item item--blue" x="413" y="806">strategies</text>
    <use href="#bullet-arrow" class="bullet--blue" x="437" y="828" width="16" height="16"/>
    <text class="item item--blue" x="461" y="836">Sport + program</text>
    <text class="item item--blue" x="461" y="854">specific strategies</text>
  </g>

  <!-- community impact services -->
  <g class="service-list service-list--impact">
    <use href="#bullet-arrow" class="bullet--blue" x="789" y="550" width="16" height="16"/>
    <text class="item item--blue item--small" x="814" y="557">Community Impact</text>
    <text class="item item--blue item--small" x="814" y="572">monitoring</text>
    <use href="#bullet-arrow" class="bullet--blue" x="789" y="595" width="16" height="16"/>
    <text class="item item--blue item--small" x="814" y="608">Contract Monitoring</text>
    <use href="#bullet-arrow" class="bullet--blue" x="789" y="633" width="16" height="16"/>
    <text class="item item--blue item--small" x="814" y="645">Social value</text>
    <use href="#bullet-arrow" class="bullet--blue" x="789" y="678" width="16" height="16"/>
    <text class="item item--blue item--small" x="814" y="683">Community out-</text>
    <text class="item item--blue item--small" x="814" y="698">comes + KPIs</text>
  </g>
</svg>
</body>
</html>
```